Create modern and sleek business card for luxury real estate company

We're a "boutique" real estate office looking for a design that gets across a highly modern luxury brand. Blacks and whites are probably the best colors unless we try a silver foil for the logo. I've attached a version of our current logo here. I'd like to swap out the current font on there with Gotham Light Regular.

I'm looking to have one side of the card have the logo with the space for our agents info on the other side.

Target Market(s)

Young professionals in a "luxury" headspace

Industry/Entity Type

Real estate

Contact Information for Business Card

A place for agent name, cell number, website. The slogan "Simply Rethinking Real Estate".

Font styles to use
Other font styles liked:
• Gotham Regular

Colors

Designer to choose only greyscale colors for use in the design.

Requirements
Must have
• Matte black as the background color. Clean lines and use of contrast. A specific design aspect that will use silver foil.
Nice to have
• Up in the air on integrating a QR code
Should not have
• Any houses or other real estate related design (ex: a clip art house)

```html
<!DOCTYPE html>
<html lang="en">
<head>
<meta charset="utf-8">
<title>Halden Realty — Business Card</title>
<link rel="stylesheet" href="https://fonts.googleapis.com/css2?family=Cinzel:wght@500&family=Lato:wght@400&display=swap">
<style>
  :root {
    --matte-black: #333333;
    --paper-white: #ffffff;
    --ink: #1c1c1c;
    --silver: #f2f2f2;
    --stage: #e6e6e6;
    --card-shadow: rgba(0, 0, 0, 0.25);
  }
  * { box-sizing: border-box; margin: 0; padding: 0; }
  html, body {
    width: 1200px;
    height: 900px;
    overflow: hidden;
    background: var(--stage);
  }
  .canvas {
    width: 1200px;
    height: 900px;
    display: flex;
    flex-direction: column;
    align-items: center;
    justify-content: center;
    gap: 60px;
  }
  .card {
    position: relative;
    width: 560px;
    height: 320px;
    overflow: hidden;
    box-shadow: 0 8px 22px var(--card-shadow);
  }

  /* Front */
  .card--front {
    background: var(--matte-black);
    display: flex;
    align-items: center;
    justify-content: center;
  }
  .brand {
    display: flex;
    align-items: center;
    gap: 18px;
  }
  .brand__circle {
    border-radius: 50%;
    flex: none;
  }
  .brand__name {
    font-family: "Cinzel", serif;
    font-weight: 500;
    line-height: 1.05;
    letter-spacing: 0.02em;
  }
  .card--front .brand__circle {
    width: 92px;
    height: 92px;
    border: 3px solid var(--silver);
  }
  .card--front .brand__name {
    color: var(--silver);
    font-size: 40px;
  }
  .brand__name span { display: block; }
  .brand__name span + span { padding-left: 34px; }

  /* Back */
  .card--back { background: var(--paper-white); }
  .card__wave {
    position: absolute;
    inset: 0;
    width: 100%;
    height: 100%;
  }
  .wave__band { fill: var(--matte-black); }
  .wave__line { fill: none; stroke: var(--paper-white); stroke-width: 3; }

  .agent {
    position: absolute;
    left: 34px;
    top: 44px;
    color: var(--ink);
  }
  .agent__name {
    font-family: "Cinzel", serif;
    font-weight: 500;
    font-size: 24px;
    letter-spacing: 0.02em;
    line-height: 1;
  }
  .agent__title {
    font-family: "Lato", sans-serif;
    font-size: 13px;
    margin-top: 3px;
  }
  .card--back .brand {
    position: absolute;
    right: 26px;
    top: 36px;
    gap: 12px;
  }
  .card--back .brand__circle {
    width: 60px;
    height: 60px;
    border: 2.5px solid var(--ink);
  }
  .card--back .brand__name {
    color: var(--ink);
    font-size: 25px;
  }
  .card--back .brand__name span + span { padding-left: 22px; }

  .contact {
    position: absolute;
    left: 34px;
    top: 140px;
    list-style: none;
    font-family: "Lato", sans-serif;
    font-size: 14px;
    color: var(--ink);
  }
  .contact__item {
    display: flex;
    align-items: center;
    gap: 9px;
    line-height: 1.45;
  }
  .contact__icon { width: 14px; height: 14px; flex: none; }
  .contact__address {
    margin-top: 12px;
    line-height: 1.35;
  }
  .website {
    position: absolute;
    right: 30px;
    bottom: 36px;
    font-family: "Lato", sans-serif;
    font-size: 13px;
    color: var(--paper-white);
    letter-spacing: 0.02em;
  }
</style>
</head>
<body>
<main class="canvas">

  <section class="card card--front" aria-label="Card front">
    <div class="brand">
      <div class="brand__circle"></div>
      <p class="brand__name"><span>Halden</span><span>Realty</span></p>
    </div>
  </section>

  <section class="card card--back" aria-label="Card back">
    <svg class="card__wave" viewBox="0 0 560 320" preserveAspectRatio="none" aria-hidden="true">
      <path class="wave__band" d="M0,262 C190,262 330,245 440,172 C490,142 528,134 560,132 V320 H0 Z"/>
      <path class="wave__line" d="M0,286 C190,284 300,268 405,196"/>
    </svg>

    <div class="agent">
      <h1 class="agent__name">Marcus Hale</h1>
      <p class="agent__title">Managing Director</p>
    </div>

    <div class="brand">
      <div class="brand__circle"></div>
      <p class="brand__name"><span>Halden</span><span>Realty</span></p>
    </div>

    <ul class="contact">
      <li class="contact__item">
        <svg class="contact__icon" viewBox="0 0 24 24" aria-hidden="true"><path fill="currentColor" d="M6.6 10.8a15.1 15.1 0 0 0 6.6 6.6l2.2-2.2a1 1 0 0 1 1-.25 11.4 11.4 0 0 0 3.6.57 1 1 0 0 1 1 1V20a1 1 0 0 1-1 1A17 17 0 0 1 3 4a1 1 0 0 1 1-1h3.5a1 1 0 0 1 1 1c0 1.25.2 2.45.57 3.57a1 1 0 0 1-.25 1z"/></svg>
        <span>044-555 018 204</span>
      </li>
      <li class="contact__item">
        <svg class="contact__icon" viewBox="0 0 24 24" aria-hidden="true"><path fill="currentColor" d="M2 5h20v14H2zm2 2v.5l8 5 8-5V7zm0 3v7h16v-7l-8 5z"/></svg>
        <span>info@haldenrealty.com</span>
      </li>
      <li class="contact__address">17, Larkspur Row<br>Westbrook, 45190</li>
    </ul>

    <p class="website">www.haldenrealty.com</p>
  </section>

</main>
</body>
</html>
```